Business Card Design Project

KV Strategy Partners is a management consulting business with C-suite (CEO/CFO etc) target clients. Logo selected is blue with simple/serious typefaces.

Target Market(s)

CEOs and CFOs of large corporates

Industry/Entity Type

Management Consulting

Font styles to use
Serif

Colors
3276b5

Requirements
Must have
• Tag line: Shaping lasting client partnerships (use different font)
Address: 457 Cedar Brook Lane #03-22 Singapore 519307
Telephone: +65 8372 6094
Email: kvlorne@mailbox47.com

```html
<!DOCTYPE html>
<html lang="en">
<head>
<meta charset="utf-8">
<title>KV Strategy Partners – Business Cards</title>
<link href="https://fonts.googleapis.com/css2?family=Tinos:wght@400&family=Arimo:wght@400&display=swap" rel="stylesheet">
<style>
  :root {
    --backdrop: #a8a8a8;
    --brand-blue: #3276b5;
    --band-blue: #2f86c9;
    --band-edge: #1d5f96;
    --card-white: #ffffff;
    --card-dark: #16191d;
    --card-dark-mid: #24282d;
    --ink-light: #f2f2f2;
    --ink-soft: #d9dde2;
    --tagline-ink: #0c2a44;
  }
  * { box-sizing: border-box; margin: 0; padding: 0; }
  html, body {
    width: 1200px;
    height: 900px;
    overflow: hidden;
    background: var(--backdrop);
  }
  .canvas {
    position: relative;
    width: 1200px;
    height: 900px;
    display: flex;
    align-items: center;
    justify-content: center;
    gap: 60px;
  }
  .card {
    position: relative;
    width: 510px;
    height: 300px;
    border-radius: 24px;
    overflow: hidden;
    box-shadow: 0 14px 30px rgba(0, 0, 0, 0.28);
  }

  /* Front card */
  .card--front { background: var(--card-white); }
  .front__brand {
    position: absolute;
    left: 30px;
    top: 0;
    height: 138px;
    display: flex;
    align-items: center;
  }
  .brand-name {
    font-family: "Tinos", "Times New Roman", serif;
    font-weight: 400;
    font-variant: small-caps;
    color: var(--brand-blue);
    letter-spacing: 0.5px;
    white-space: nowrap;
  }
  .front__brand .brand-name { font-size: 44px; }

  .tagline-band {
    position: absolute;
    left: 0;
    right: 0;
    top: 138px;
    height: 17px;
    background: linear-gradient(180deg, var(--band-blue), var(--band-edge));
    display: flex;
    align-items: center;
    padding-left: 30px;
  }
  .tagline {
    font-family: "Arimo", "Helvetica", sans-serif;
    font-size: 11px;
    letter-spacing: 6px;
    color: var(--tagline-ink);
    white-space: nowrap;
  }
  .front__details {
    position: absolute;
    left: 0;
    right: 0;
    top: 155px;
    bottom: 0;
    background: linear-gradient(180deg, var(--card-dark-mid), var(--card-dark));
    padding: 22px 30px;
  }
  .contact-list {
    list-style: none;
    font-family: "Tinos", "Times New Roman", serif;
    font-size: 16px;
    line-height: 21px;
    color: var(--ink-light);
  }
  .contact-list li {
    display: flex;
    align-items: flex-start;
    gap: 5px;
  }
  .contact-icon {
    width: 13px;
    height: 13px;
    margin-top: 4px;
    flex: none;
    fill: var(--band-blue);
  }
  .contact-address { padding-left: 18px; }

  /* Back card */
  .card--back {
    background: radial-gradient(ellipse at 50% 30%, #34393f 0%, var(--card-dark-mid) 40%, var(--card-dark) 100%);
    display: flex;
    align-items: center;
    justify-content: center;
  }
  .card--back .brand-name {
    font-size: 46px;
    color: var(--ink-soft);
  }
</style>
</head>
<body>
<main class="canvas">
  <section class="card card--front" aria-label="Business card front">
    <div class="front__brand">
      <span class="brand-name">KV Strategy Partners</span>
    </div>
    <div class="tagline-band">
      <p class="tagline">Shaping lasting client partnerships</p>
    </div>
    <div class="front__details">
      <ul class="contact-list">
        <li>
          <svg class="contact-icon" viewBox="0 0 16 16" aria-hidden="true"><path d="M3.2 1.2l2.4 2.9-1.3 1.6c.9 2 2.4 3.6 4.4 4.6l1.6-1.3 2.9 2.3-1.4 2.5C6.9 13.4 2.5 9.1 1 3.3z"/></svg>
          <span>+65 8372 6094</span>
        </li>
        <li>
          <svg class="contact-icon" viewBox="0 0 16 16" aria-hidden="true"><path d="M1 3.5h14v9H1z M1.8 4.2L8 9l6.2-4.8" stroke="#16191d" stroke-width="1"/></svg>
          <span>kvlorne@mailbox47.com</span>
        </li>
        <li>
          <svg class="contact-icon" viewBox="0 0 16 16" aria-hidden="true"><path d="M8 1.5L1 8h2v6.5h4v-4h2v4h4V8h2z"/></svg>
          <span>457 Cedar Brook Lane #03-22</span>
        </li>
        <li class="contact-address">Singapore 519307</li>
      </ul>
    </div>
  </section>

  <section class="card card--back" aria-label="Business card back">
    <span class="brand-name">KV Strategy Partners</span>
  </section>
</main>
</body>
</html>
```